VELUNDO Brisbane Tiling Service

My name is Mirko Bostel i need a business card for a new company. We are wall and floor tilers based in Brisbane, our company is Velundio Brisbane Tiling Service.
We would like a logo from our website used on our cards. Our website is www.velundio.com.au

I would like my Facebook and Twitter accounts on my card.

Industry/Entity Type

Business

Colors
0692cd
3176b5
33a6d7
85cae6

```html
<!DOCTYPE html>
<html lang="en">
<head>
<meta charset="utf-8">
<title>Velundio Brisbane Tiling Service – Business Card</title>
<link rel="stylesheet" href="https://fonts.googleapis.com/css2?family=Arimo:wght@400;700&display=swap">
<style>
  :root {
    --brand-blue: #0692cd;
    --brand-blue-deep: #1a7fc0;
    --brand-blue-mid: #3176b5;
    --brand-blue-light: #85cae6;
    --card-white: #ffffff;
    --card-tint: #eef0f2;
    --stage: #e4e6e8;
    --text-white: #ffffff;
  }
  * { box-sizing: border-box; margin: 0; padding: 0; }
  html, body {
    width: 1200px; height: 900px; overflow: hidden;
    background: var(--stage);
    font-family: "Arimo", Arial, sans-serif;
  }
  .canvas {
    position: relative; width: 1200px; height: 900px;
  }
  .card {
    position: absolute; width: 500px; height: 286px;
    background: linear-gradient(160deg, var(--card-white) 0%, var(--card-tint) 100%);
    box-shadow: 0 6px 18px rgba(0,0,0,0.18);
    overflow: hidden;
  }
  .card--front { left: 70px; top: 307px; }
  .card--back { left: 630px; top: 307px; }

  /* front */
  .brand {
    position: absolute; left: 34px; bottom: 40px;
    display: flex; align-items: flex-end; gap: 12px;
  }
  .brand__square {
    width: 70px; height: 70px; border-radius: 6px; background: var(--brand-blue-deep);
  }
  .brand__text { display: flex; flex-direction: column; }
  .brand__name {
    color: var(--brand-blue-deep); font-size: 58px; line-height: 0.9; font-weight: 400; letter-spacing: 0.5px;
  }
  .brand__tagline {
    color: var(--brand-blue-deep); font-size: 20px; line-height: 1.2; margin-top: 4px;
  }

  /* back */
  .band {
    position: absolute; left: 0; right: 0; top: 62px; height: 138px;
    background: var(--brand-blue-deep);
  }
  .band__name {
    position: absolute; left: 0; width: 190px; top: 0; height: 138px;
    display: flex; align-items: center; justify-content: center;
    color: var(--text-white); font-size: 30px; font-weight: 700;
  }
  .band__divider {
    position: absolute; left: 190px; top: 18px; bottom: 18px; width: 2px; background: var(--text-white);
  }
  .contact {
    position: absolute; left: 216px; top: 14px; color: var(--text-white);
  }
  .contact__person { font-size: 25px; margin-bottom: 16px; }
  .contact__line {
    display: flex; align-items: center; gap: 9px; font-size: 13px; line-height: 19px;
  }
  .contact__line svg { width: 11px; height: 11px; fill: var(--text-white); }
  .social {
    position: absolute; left: 216px; top: 206px; color: var(--brand-blue-deep);
  }
  .social__line {
    display: flex; align-items: center; gap: 8px; font-size: 13px; line-height: 19px;
  }
  .social__mark { width: 11px; height: 11px; background: var(--brand-blue-deep); border-radius: 2px; }
</style>
</head>
<body>
<main class="canvas">
  <section class="card card--front" aria-label="Card front">
    <div class="brand">
      <span class="brand__square"></span>
      <div class="brand__text">
        <span class="brand__name">velundio</span>
        <span class="brand__tagline">brisbane tiling service</span>
      </div>
    </div>
  </section>

  <section class="card card--back" aria-label="Card back">
    <div class="band">
      <div class="band__name">velundio</div>
      <div class="band__divider"></div>
      <div class="contact">
        <p class="contact__person">Mirko Bostel</p>
        <p class="contact__line">
          <svg viewBox="0 0 12 12"><path d="M2.5 0.5 L4.5 0.5 L5.3 3 L4 4.2 Q5 6.8 7.8 8 L9 6.7 L11.5 7.5 L11.5 9.5 Q11 11.5 9 11.5 Q1 10.5 0.5 3 Q0.5 1 2.5 0.5Z"/></svg>
          0400 562 318
        </p>
        <p class="contact__line">
          <svg viewBox="0 0 12 12"><path d="M0 2 H12 V10 H0Z M0.8 2.8 L6 6.6 L11.2 2.8" stroke="#1a7fc0" stroke-width="0.9"/></svg>
          info@velundio.com.au
        </p>
        <p class="contact__line">
          <svg viewBox="0 0 12 12"><path d="M6 0.5 L11.5 5.5 H10 V11.5 H7.3 V8 H4.7 V11.5 H2 V5.5 H0.5Z"/></svg>
          www.velundio.com.au
        </p>
      </div>
    </div>
    <div class="social">
      <p class="social__line"><span class="social__mark"></span>/Velundio-Brisbane-Tiling-Service</p>
      <p class="social__line"><span class="social__mark"></span>/infovelundio</p>
    </div>
  </section>
</main>
</body>
</html>
```